Business Stationery design
Letterhead, compliments slip, business card x 2, email signature
Business Stationery design - Health
Creative Brief
A new design of letterhead required following our rebranding excercise which started with a new logo
Health
Patients, corporate
1. We require a letterhead for A4 paper, this must be contemporary and modern in design using the logo attached somewhere in the design. 2. We require a design for a compliments slip 99mm x 210mm, this can be portrait or landscape, using the logo attached and reflecting the design of the letterhead. 3. We require 2 designs of business cards - one which will be printed on clear plastic and one will be on card, the card one can be double sided. The information for the business card is a follows: Roderick Penhale B.Sc., MCOptom, F.B.D.O., Dip.O.D., OPwSI Principal Clinical Optometrist The business information for all three is: Address: 14 Tarrow Lane, Snodland, Kent ME4 2QX Telephone: 01632 918372 Email: info@clearviewsample.co.uk Web Address: www.clearviewsample.co.uk Additional information for the letterhead which can be 8pt: Registered Office: Harlow Penrose Judd, Brenton House, Vell Street, Dover, Kent CT12 7RW Company Registered in England and Wales: 09381726 Finally - 4: an email signature using the logo address etc
Roderick Roderick
OK, again great designs but no-one seems to have listened the the problem that we cannot have a bleed on the A4 paper. It is probably therefore best to have 2 designs for the A4 paper - one with a bleed and one without. This is because we do have some A4 paper printed and some is printed as a mailshot is done by an outside source and they do not have the ability to bleed off the edge of the paper - please modify your designs
Thank you all for your designs, design No 24 has the correct formatting for the name and qualifications etc which should be Roderick Penhale B.Optom., F.C.O.S., Dip.C.L., Cert.G.P. Principal Clinical Optometrist (copy and paste the above and the lines etc should be correct) At the moment I favour design 16. I think that the curves have been done to death by every company so we need to stay away from that now please unless you have something cutting edge and amazing! Many thanks
Also the letterhead cannot include a bleed, unless you do a design with and without a bleed as some mailings are printed and mailed offsite and they do not have the ability to bleed at present
OK designs are looking good so far, I have rated them. However I want to lose the corporate look a little as we are an independent practice. Also the formatting for the name, qualifications etc should be: Roderick Penhale B.Optom., F.C.O.S., Dip.C.L., Cert.G.P. Principal Clinical Optometrist

```html
<!DOCTYPE html>
<html lang="en">
<head>
<meta charset="utf-8">
<title>Clearview Optometrists – Business Card</title>
<link rel="stylesheet" href="https://fonts.googleapis.com/css2?family=Source+Sans+3:wght@300;400;600&display=swap">
<style>
  :root {
    --page-bg: #e9e7e4;
    --blue-deep: #123f8c;
    --blue-mid: #2a5db0;
    --blue-light: #3f78c9;
    --blue-tab: #5c8fd6;
    --band-blue: #1d4690;
    --ink: #1c1c1c;
    --ink-soft: #555;
    --white: #ffffff;
    --tab-grey-a: #f2f2f2;
    --tab-grey-b: #bdbdbd;
    --rule: #9a9a9a;
  }
  * { margin: 0; padding: 0; box-sizing: border-box; }
  html, body { width: 1200px; height: 900px; overflow: hidden; }
  body {
    background: var(--page-bg);
    font-family: "Source Sans 3", "Myriad Pro", Arial, sans-serif;
    position: relative;
  }
  .card {
    position: absolute;
    left: 297px;
    width: 606px;
    height: 326px;
    border-radius: 22px;
    overflow: hidden;
    box-shadow: 0 10px 24px rgba(0,0,0,0.25);
  }
  .card--front {
    top: 100px;
    background: radial-gradient(ellipse at 50% 45%, var(--blue-light) 0%, var(--blue-mid) 45%, var(--blue-deep) 100%);
    color: var(--white);
  }
  .card--back {
    top: 474px;
    background: var(--white);
    color: var(--ink);
  }
  .tab {
    position: absolute;
    top: 0;
    left: 166px;
    width: 278px;
    height: 20px;
    border-radius: 0 0 6px 6px;
  }
  .card--front .tab { background: var(--blue-tab); opacity: 0.75; }
  .card--back .tab { background: linear-gradient(var(--tab-grey-a), var(--tab-grey-b)); }

  .brand {
    position: absolute;
    left: 0; right: 0;
    text-align: center;
    font-weight: 400;
    line-height: 1;
  }
  .card--front .brand { top: 140px; }
  .brand__name { display: block; }
  .card--front .brand__name { font-size: 66px; letter-spacing: -1px; }
  .card--front .brand__sub { display: block; font-size: 26px; letter-spacing: 4px; margin-top: 4px; }

  .web-band {
    position: absolute;
    bottom: 0;
    left: 166px;
    width: 278px;
    height: 30px;
    background: var(--band-blue);
    border-radius: 6px 6px 0 0;
    font-size: 16px;
    line-height: 30px;
    text-align: center;
    color: var(--white);
  }

  .card--back .brand { top: 58px; color: var(--blue-deep); }
  .card--back .brand__name { font-size: 30px; letter-spacing: -0.5px; }
  .card--back .brand__sub { display: block; font-size: 12px; letter-spacing: 2px; margin-top: 2px; }

  .person {
    position: absolute;
    top: 152px;
    left: 0; right: 0;
    text-align: center;
  }
  .person__name { font-size: 32px; font-weight: 400; line-height: 1; }
  .person__quals, .person__role { font-size: 11.5px; color: var(--ink-soft); line-height: 1.35; }
  .person__quals { margin-top: 6px; }
  .rule {
    width: 170px;
    height: 1px;
    background: var(--rule);
    margin: 10px auto 12px;
  }
  .contact { font-size: 11.5px; color: var(--ink-soft); line-height: 1.45; }

  .email-band {
    position: absolute;
    bottom: 0;
    left: 164px;
    width: 320px;
    height: 30px;
    background: var(--band-blue);
    border-radius: 8px 8px 0 0;
    color: var(--white);
    font-size: 17px;
    line-height: 30px;
    text-align: center;
  }
</style>
</head>
<body>
  <section class="card card--front">
    <div class="tab"></div>
    <div class="brand">
      <span class="brand__name">Clearview</span>
      <span class="brand__sub">OPTOMETRISTS</span>
    </div>
    <div class="web-band">www.clearviewsample.co.uk</div>
  </section>

  <section class="card card--back">
    <div class="tab"></div>
    <div class="brand">
      <span class="brand__name">Clearview</span>
      <span class="brand__sub">OPTOMETRISTS</span>
    </div>
    <div class="person">
      <h1 class="person__name">Roderick Penhale</h1>
      <p class="person__quals">B.Optom., F.C.O.S., Dip.C.L., Cert.G.P.</p>
      <p class="person__role">Principal Clinical Optometrist</p>
      <div class="rule"></div>
      <p class="contact">A: 14 Tarrow Lane, Ashcombe, Wessex ME4 2QX<br>T: 01632 918372</p>
    </div>
    <div class="email-band">info@clearviewsample.co.uk</div>
  </section>
</body>
</html>
```